Photography and Videography - Tidewell Studios - New Business Card Design

Tidewell Studios is a photography and Videography Company started by creative couple Rory K and Lena P and based on the Sunshine Coast in Queensland, Australia.
We're quirky, creative and innovative people and would like a business card that keeps you looking for more than just a few seconds.
Design wise we would like a black or charcoal background with a bit of a funkier design than just a boring old rectangle shape. Perhaps curved on an edge.
Ideally we would like to be able to make a collage of all of our best photos on the reverse side of the card with the company name or logo and "catch you by the tidewell..." (possibly in italics) underneath it.
On the front of the business card we would like our company name -
"Tidewell Studios", our motto- "Bringing Ideas To Life..." (possibly in italics) and our contact information. The background should be a darker colour like black or charcoal.
We like the look of having contact company details and contact info to one side (right) and a black and white photo of Rory K and Lena P to the other side (left).
Thank you and Good Luck!
Industry/Entity Type
Business
Contact Information for Business Card
Business Name - Tidewell Studios
Slogan - Bring Ideas To life
Name - Rory K | Lena P
Description - Photography | Videography
Phone - 0452 867 213 | 0438 926 057
Email - tidewellstudios@mailbox-example.com.au
Website - www.tidewellstudios-example.com.au
Like us on Friendbook (symbol)
Logo styles of interest
Pictorial/Combination Logo
Look and feel

```html
<!DOCTYPE html>
<html lang="en">
<head>
<meta charset="utf-8">
<title>Tidewell Studios – Business Card</title>
<link rel="stylesheet" href="https://fonts.googleapis.com/css2?family=Bebas+Neue&family=Dancing+Script:wght@400;500&family=Open+Sans:wght@400&family=Sacramento&display=swap">
<style>
  :root {
    --card-black: #000000;
    --paper: #ffffff;
    --ink: #ffffff;
    --photo-light: #a9ad9c;
    --photo-mid: #5d6155;
    --photo-dark: #1c1d19;
    --badge: #3a3a3a;
  }
  * { margin: 0; padding: 0; box-sizing: border-box; }
  html, body { width: 1200px; height: 741px; overflow: hidden; background: var(--paper); }
  .card {
    position: relative;
    width: 1200px;
    height: 741px;
    background: var(--card-black);
    color: var(--ink);
    font-family: "Open Sans", Arial, sans-serif;
    overflow: hidden;
  }
  .card-notch { position: absolute; inset: 0; width: 1200px; height: 741px; }
  .couple-photo {
    position: absolute;
    left: 0; top: 0;
    width: 440px; height: 741px;
    background:
      radial-gradient(ellipse at 35% 40%, var(--photo-light) 0%, var(--photo-mid) 45%, transparent 80%),
      linear-gradient(90deg, var(--photo-mid) 0%, var(--photo-dark) 70%, var(--card-black) 100%);
  }
  .brand-column {
    position: absolute;
    left: 424px;
    bottom: 6px;
    writing-mode: vertical-rl;
    transform: rotate(180deg);
    display: flex;
    align-items: baseline;
    gap: 6px;
    white-space: nowrap;
  }
  .brand-name {
    font-family: "Bebas Neue", Impact, sans-serif;
    font-size: 53px;
    letter-spacing: 1px;
    line-height: 1;
  }
  .brand-motto {
    font-family: "Dancing Script", cursive;
    font-size: 33px;
    line-height: 1;
  }
  .social {
    position: absolute;
    left: 733px;
    top: 30px;
    display: flex;
    align-items: center;
    gap: 14px;
    font-size: 27px;
  }
  .social-badge {
    width: 56px; height: 56px;
    border-radius: 8px;
    background: var(--badge);
  }
  .owners {
    position: absolute;
    left: 548px;
    top: 238px;
    font-family: "Sacramento", cursive;
    font-size: 84px;
    line-height: 1;
  }
  .services {
    position: absolute;
    left: 568px;
    top: 338px;
    font-family: "Sacramento", cursive;
    font-size: 52px;
    font-weight: 400;
    line-height: 1;
  }
  .contact {
    position: absolute;
    right: 41px;
    top: 520px;
    text-align: right;
    font-size: 31px;
    line-height: 50px;
  }
  .phone-group { display: flex; justify-content: flex-end; align-items: center; gap: 12px; }
  .phone-label {
    writing-mode: vertical-rl;
    transform: rotate(180deg);
    font-size: 19px;
    line-height: 1;
  }
  .contact-line { display: block; }
</style>
</head>
<body>
  <div class="card">
    <div class="couple-photo" role="img" aria-label="Black and white photo of Rory K and Lena P posing together"></div>

    <svg class="card-notch" viewBox="0 0 1200 741" aria-hidden="true">
      <path d="M1008 0 C1018 40 1002 100 1030 122 C1060 140 1150 126 1200 150 L1200 0 Z" fill="#ffffff"/>
    </svg>

    <div class="brand-column">
      <span class="brand-name">TIDEWELL STUDIOS</span>
      <span class="brand-motto">Bringing ideas to life...</span>
    </div>

    <div class="social">
      <span class="social-text">Like us on Friendbook</span>
      <span class="social-badge" aria-hidden="true"></span>
    </div>

    <h1 class="owners">Rory K &amp; Lena P</h1>
    <p class="services">Photography | Videography</p>

    <div class="contact">
      <div class="phone-group">
        <span class="phone-label">Phone</span>
        <div>
          <span class="contact-line">0452-867-213</span>
          <span class="contact-line">0438-926-057</span>
        </div>
      </div>
      <span class="contact-line">tidewellstudios@mailbox-example.com</span>
      <span class="contact-line">www.tidewellstudios-example.com.au</span>
    </div>
  </div>
</body>
</html>
```